New business card for civil engineering company - "Keystone Audit"

We need a business card designed for our new structural engineering company.

The company name is "Keystone Audit" logo files attached.

We would like the following:
* Two-sided card
* Simple design

Information to be placed on the card:
Name - Marcus Dellow
Job Title - Director / Structural Engineer
Credentials - BEng(Hons), CPEng, CMengNZ, IntPE(NZ)
Email - marcus.dellow@keystoneaudit.co.nz
mobile - 0219364058
website - www.keystoneaudit.co.nz

```html
<!DOCTYPE html>
<html lang="en">
<head>
<meta charset="utf-8">
<title>Keystone Audit – Business Card</title>
<link href="https://fonts.googleapis.com/css2?family=Questrial&display=swap" rel="stylesheet">
<style>
  :root {
    --board: #4d4d4d;
    --card: #000000;
    --ice: #b3f0ff;
    --sky: #8fdcff;
    --blue: #4ea2ff;
    --white: #f2f6fa;
  }
  html, body {
    margin: 0;
    padding: 0;
    overflow: hidden;
  }
  body {
    width: 848px;
    height: 1200px;
    background: var(--board);
    position: relative;
    font-family: "Questrial", sans-serif;
  }
  .card {
    position: absolute;
    left: 168px;
    width: 513px;
    height: 293px;
    background: var(--card);
  }
  .card--front { top: 229px; }
  .card--back { top: 702px; }

  .brand {
    position: absolute;
    left: 0;
    right: 0;
    top: 118px;
    text-align: center;
  }
  .brand__name {
    color: var(--ice);
    font-size: 17px;
    letter-spacing: 2.2px;
    text-transform: uppercase;
    line-height: 1;
  }
  .brand__tagline {
    margin-top: 7px;
    color: var(--ice);
    font-size: 6px;
    letter-spacing: 1.6px;
    text-transform: uppercase;
  }

  .person {
    position: absolute;
    left: 36px;
    width: 190px;
    top: 125px;
    text-align: center;
  }
  .person__name {
    color: var(--ice);
    font-size: 22px;
    letter-spacing: 1.4px;
    text-transform: uppercase;
    line-height: 1;
  }
  .person__role {
    margin-top: 8px;
    color: var(--white);
    font-size: 7.5px;
    letter-spacing: 1px;
    text-transform: uppercase;
  }

  .divider {
    position: absolute;
    left: 222px;
    top: 50px;
    width: 3.5px;
    height: 193px;
    border-radius: 2px;
    background: linear-gradient(to bottom, var(--sky), var(--blue));
  }

  .contacts {
    position: absolute;
    left: 248px;
    top: 68px;
    margin: 0;
    padding: 0;
    list-style: none;
  }
  .contact {
    position: absolute;
    left: 0;
    display: flex;
    align-items: center;
    white-space: nowrap;
  }
  .contact__icon {
    width: 20px;
    height: 20px;
    flex: none;
    color: var(--blue);
  }
  .contact__text {
    margin-left: 17px;
    color: var(--blue);
    font-size: 8.6px;
    letter-spacing: 1px;
    text-transform: uppercase;
    line-height: 1.4;
  }
  .contact--credentials { top: 0; }
  .contact--credentials .contact__text {
    text-transform: none;
    font-variant: small-caps;
    font-size: 9.5px;
    color: var(--blue);
  }
  .contact--credentials .contact__icon { color: var(--sky); }
  .contact--phone { top: 42px; }
  .contact--email { top: 86px; }
  .contact--web { top: 131px; }
  .contact--email .contact__text { letter-spacing: 0.55px; }
</style>
</head>
<body>

<section class="card card--front">
  <div class="brand">
    <div class="brand__name">Keystone Audit</div>
    <div class="brand__tagline">Peer Review Specialists</div>
  </div>
</section>

<section class="card card--back">
  <div class="person">
    <div class="person__name">Marcus Dellow</div>
    <div class="person__role">Director / Structural Engineer</div>
  </div>

  <div class="divider"></div>

  <ul class="contacts">
    <li class="contact contact--credentials">
      <svg class="contact__icon" viewBox="0 0 20 20" aria-hidden="true">
        <rect x="2" y="0" width="16" height="23" rx="1.5" fill="currentColor" transform="scale(1 0.87)"/>
        <circle cx="10" cy="5" r="2.4" fill="none" stroke="#000" stroke-width="0.9"/>
        <path d="M8.4 6.8 L7.6 9.6 M11.6 6.8 L12.4 9.6" stroke="#000" stroke-width="0.9"/>
        <path d="M5 12 H15 M5 14 H15 M5 16 H15" stroke="#000" stroke-width="0.8"/>
      </svg>
      <span class="contact__text">BEng(Hons), CPEng,<br>CMengNZ, IntPE(NZ)</span>
    </li>
    <li class="contact contact--phone">
      <svg class="contact__icon" viewBox="0 0 20 20" aria-hidden="true">
        <path fill="currentColor" d="M4.2 1.2c.7-.5 1.6-.3 2 .4l1.6 2.7c.4.7.2 1.5-.4 2l-1.1.8c.8 2.6 3 5.1 5.6 6.3l1-1c.6-.5 1.4-.6 2-.1l2.5 1.9c.6.5.7 1.4.2 2l-1.2 1.4c-.9 1-2.4 1.3-3.6.7C7.3 16.3 3.3 11.8 2 6.3c-.3-1.3.1-2.6 1.1-3.5z"/>
      </svg>
      <span class="contact__text">+64 02193 64058</span>
    </li>
    <li class="contact contact--email">
      <svg class="contact__icon" viewBox="0 0 20 20" aria-hidden="true">
        <rect x="1" y="4" width="18" height="13" rx="1" fill="currentColor"/>
        <path d="M1.5 4.8 L10 11.5 L18.5 4.8" fill="none" stroke="#000" stroke-width="1.3"/>
      </svg>
      <span class="contact__text">marcus.dellow@keystoneaudit.co.nz</span>
    </li>
    <li class="contact contact--web">
      <svg class="contact__icon" viewBox="0 0 20 20" aria-hidden="true">
        <g fill="none" stroke="currentColor" stroke-width="1.5">
          <circle cx="10" cy="10" r="8.5"/>
          <ellipse cx="10" cy="10" rx="3.8" ry="8.5"/>
          <path d="M10 1.5 V18.5 M1.5 10 H18.5 M3 5.8 H17 M3 14.2 H17"/>
        </g>
      </svg>
      <span class="contact__text">www.keystoneaudit.co.nz</span>
    </li>
  </ul>
</section>

</body>
</html>
```